sign business needs card design

I need a very clean design for my business card.
It is a sign company. Banners By Noon is the name of the business.
Our colors are orange, yellow. But I want a very professional card.
But you can use any colors. I like a black background with orange letters or a white back with a clean look. No cartoon or kiddy looking print. The info. I need on the card is as follows.
Banners By Noon
318.555.0172 ph.
318.555.0199 fax.
email.bannersbynoon@mailvista.net
web.bannersbynooninc.com
4187 N. Maplecrest Lane Ste. 2b
Dale Hutchins

```html
<!DOCTYPE html>
<html lang="en">
<head>
<meta charset="utf-8">
<title>Banners By Noon — Business Card</title>
<link rel="stylesheet" href="https://fonts.googleapis.com/css2?family=Carlito:wght@400;700&display=swap">
<style>
  :root {
    --backdrop: #92d34f;
    --card-black: #000000;
    --band-grey: #808080;
    --rule-grey: #8a8a8a;
    --ink-orange: #f0a93a;
  }
  html, body {
    margin: 0;
    padding: 0;
    width: 1200px;
    height: 739px;
    overflow: hidden;
    background: var(--backdrop);
  }
  .canvas {
    position: relative;
    width: 1200px;
    height: 739px;
    background: var(--backdrop);
    font-family: "Carlito", "Calibri", sans-serif;
    color: var(--ink-orange);
  }
  .business-card {
    position: absolute;
    left: 185px;
    top: 143px;
    width: 805px;
    height: 445px;
    background: var(--card-black);
    overflow: hidden;
  }
  .contact-grid {
    position: absolute;
    display: grid;
    grid-template-columns: auto auto;
    align-items: baseline;
    white-space: nowrap;
    line-height: 1;
    margin: 0;
  }
  .contact-grid dt, .contact-grid dd { margin: 0; }

  .online-contacts {
    right: 28px;
    top: 30px;
    column-gap: 22px;
    row-gap: 14px;
    font-size: 22px;
  }
  .online-contacts dt { font-size: 19px; }

  .divider-rule {
    position: absolute;
    left: 0;
    top: 159px;
    width: 266px;
    height: 2px;
    background: var(--rule-grey);
  }
  .name-band {
    position: absolute;
    left: 266px;
    top: 159px;
    width: 539px;
    height: 96px;
    background: var(--band-grey);
    border-radius: 0 15px 15px 0;
  }
  .brand-name {
    position: absolute;
    right: 88px;
    top: 50%;
    transform: translateY(-50%);
    font-size: 46px;
    font-weight: 700;
    white-space: nowrap;
    color: var(--ink-orange);
  }
  .address-line {
    position: absolute;
    right: 27px;
    top: 265px;
    margin: 0;
    font-size: 21px;
    line-height: 1;
    white-space: nowrap;
  }
  .phone-contacts {
    right: 27px;
    top: 340px;
    column-gap: 36px;
    row-gap: 20px;
    font-size: 22px;
  }
  .phone-contacts dt { font-size: 20px; }
</style>
</head>
<body>
<div class="canvas">
  <section class="business-card" aria-label="Banners By Noon business card">
    <dl class="contact-grid online-contacts">
      <dt>Emil :</dt>
      <dd>bannersbynoon@mailvista.net</dd>
      <dt>Web :</dt>
      <dd>bannersbynooninc.com</dd>
    </dl>

    <div class="divider-rule"></div>
    <div class="name-band">
      <span class="brand-name">Banners By Noon</span>
    </div>

    <p class="address-line">4187 N. Maplecrest Lane Ste. 2b Dale Hutchins</p>

    <dl class="contact-grid phone-contacts">
      <dt>Ph.</dt>
      <dd>318.555.0172</dd>
      <dt>Fax.</dt>
      <dd>318.555.0199</dd>
    </dl>
  </section>
</div>
</body>
</html>
```